Tide Harbor Brochure for on call home care staffing

Brochure to describe Tide harbor services. Tide harbor provides after hours on-call staffing and scheduling only for home care agencies. We are 100% US Based with real agents in person answering calls. We act as an extension of their agency and integrate seamlessly. I dropped in my attempt at the brochure but my AI images suck. We want realistic images with an Americana feel. I also don't want the gold color or the same images on the new one. Feel free to redo the writing.

Target Market(s)

home care agencies

Industry/Entity Type

Health care staffing

Font styles to use
Serif
Sans Serif

Colors
0054AA
0677BA
7BADD7
CADEEF
E8F1F8

Requirements
Must have
• Catchy headlines
Nice to have
• I'd like to see professional style brochure with squares integrated in.
Should not have
• VIBRANT COLORS

```html
<!DOCTYPE html>
<html lang="en">
<head>
<meta charset="utf-8">
<title>Tide Harbor – On Call Home Care Staffing Brochure</title>
<link rel="stylesheet" href="https://fonts.googleapis.com/css2?family=Exo+2:wght@600;700;800;900&family=Sarabun:wght@400;500;600&display=swap">
<style>
  :root{
    --stage:#111111;
    --paper:#ffffff;
    --navy:#163560;
    --ink:#1b1b1b;
    --body:#444a52;
    --blue:#0d4ea8;
    --blue-deep:#0a3c8e;
    --blue-band:#1152ad;
    --blue-head:#0f4aa3;
    --sky:#7badd7;
    --pale:#e8f1f8;
    --line:#cadeef;
  }
  *{box-sizing:border-box;margin:0;padding:0}
  html,body{width:790px;height:1200px;overflow:hidden;background:var(--stage)}
  .canvas{position:relative;width:790px;height:1200px;background:var(--stage);font-family:"Sarabun",sans-serif}
  .sheet{position:absolute;left:65px;width:660px;height:510px;display:flex}
  .sheet--outside{top:65px}
  .sheet--inside{top:625px}
  .panel{position:relative;width:220px;height:510px;overflow:hidden;background:var(--paper)}
  .panel--blue{background:linear-gradient(180deg,var(--blue) 0%,#0e4aa0 55%,var(--blue-deep) 100%);color:#fff;text-align:center}
  .photo{position:absolute}
  .abs{position:absolute}

  /* outside – left */
  .team-photo{left:0;top:0;width:220px;height:223px;background:linear-gradient(160deg,#6b6a66 0%,#a9a59c 45%,#5a544c 100%)}
  .intro-head{left:19px;top:177px;width:195px;height:50px;background:var(--paper);padding:14px 0 0 17px;
    font-family:"Exo 2",sans-serif;font-weight:700;font-size:12.4px;line-height:18px;color:var(--navy)}
  .intro-copy{left:19px;top:232px;width:180px;font-size:8.6px;line-height:14.8px;color:var(--body);text-align:justify}
  .intro-copy p+p{margin-top:14.8px}

  /* outside – middle */
  .cover-title{top:18px;left:0;width:220px;font-family:"Exo 2",sans-serif;font-weight:800;line-height:1}
  .cover-title .l1{display:block;font-size:24px}
  .cover-title .l2{display:block;font-size:29px;margin-top:4px}
  .cover-sub{top:85px;left:0;width:220px;font-size:11.5px;line-height:17px}
  .icon-tile{left:88px;width:44px;height:44px;background:#fff;display:flex;align-items:center;justify-content:center}
  .info-label{left:0;width:220px;font-size:8.8px;line-height:15px}
  .support-big{top:415px;left:0;width:220px;font-family:"Exo 2",sans-serif;font-weight:800;font-size:15.5px}
  .call-box{left:22px;top:453px;width:176px;height:44px;background:#fff;text-align:left}
  .call-box .tile{position:absolute;left:8px;top:6px;width:29px;height:32px;background:var(--blue);display:flex;align-items:center;justify-content:center}
  .call-box .lbl{position:absolute;left:48px;top:11px;font-size:4.5px;color:var(--ink)}
  .call-box .num{position:absolute;left:47px;top:16px;font-family:"Exo 2",sans-serif;font-weight:800;font-size:18px;color:var(--blue);letter-spacing:.2px}

  /* outside – right */
  .agent-photo{left:0;top:0;width:220px;height:371px;background:linear-gradient(150deg,#3a2a1f 0%,#6a4a32 45%,#2b2320 100%)}
  .brand-tile{left:46px;top:325px;width:111px;height:80px;background:var(--paper);display:flex;align-items:center;justify-content:center;gap:6px}
  .brand-tile .sq{width:14px;height:14px;background:var(--navy)}
  .brand-tile .name{font-family:"Exo 2",sans-serif;font-weight:700;font-size:12px;color:var(--navy)}
  .brand-name{top:397px;left:0;width:220px;text-align:center;font-family:"Exo 2",sans-serif;font-weight:800;font-size:20px;letter-spacing:1.6px;color:var(--navy)}
  .brand-line{top:431px;left:0;width:220px;text-align:center;font-family:"Exo 2",sans-serif;font-weight:800;font-size:22.5px;color:var(--ink)}
  .rule{height:1px;background:linear-gradient(90deg,transparent,var(--blue) 50%,transparent)}
  .tagline{top:468px;left:0;width:220px;text-align:center;font-size:10.5px;color:#333}

  /* inside – left */
  .sec-head{left:17px;font-family:"Exo 2",sans-serif;font-weight:800;font-size:15.5px;color:var(--ink)}
  .service{left:18px;width:184px;height:62px;background:var(--paper);border:1px solid #e3e7ec;box-shadow:0 3px 6px rgba(40,90,160,.12)}
  .service .tile{position:absolute;left:6px;top:6px;width:50px;height:50px;background:var(--blue);display:flex;align-items:center;justify-content:center}
  .service h3{position:absolute;left:69px;top:9px;font-family:"Exo 2",sans-serif;font-weight:700;font-size:8.6px;color:var(--ink)}
  .service p{position:absolute;left:69px;top:23px;width:108px;font-size:6.6px;line-height:9.8px;color:#555}
  .matters-copy{left:19px;top:301px;width:181px;font-size:7.1px;line-height:12px;color:var(--body);text-align:justify}
  .matters-copy p+p{margin-top:12px}

  /* inside – middle */
  .band-top{left:0;top:0;width:220px;height:41px;background:var(--blue-band);font-family:"Exo 2",sans-serif;font-weight:800;font-size:18px;line-height:41px;color:#fff}
  .headset-photo{left:0;top:41px;width:220px;height:329px;background:linear-gradient(160deg,#dfe7ee 0%,#b9a08a 45%,#7d8a6c 100%)}
  .band-bottom{left:0;top:370px;width:220px;height:140px;background:var(--blue-band)}
  .support-note{top:384px;left:0;width:220px;font-family:"Exo 2",sans-serif;font-weight:700;font-size:9.6px;line-height:15px;letter-spacing:.2px}
  .real{left:10px;top:418px;font-family:"Exo 2",sans-serif;font-weight:900;font-size:51px;line-height:1;letter-spacing:-1px}
  .real-list{left:149px;top:424px;text-align:left;font-family:"Exo 2",sans-serif;font-weight:700;font-size:9.6px;line-height:15px}
  .rule--light{background:#cfe0f3}
  .every{top:480px;left:0;width:220px;font-size:10.5px}

  /* inside – right */
  .empower{top:8px;left:0;width:220px;text-align:center;font-family:"Exo 2",sans-serif;font-weight:800;font-size:19.5px;line-height:25.5px;color:var(--blue-head)}
  .empower-copy{top:92px;left:0;width:220px;text-align:center;font-size:8.8px;line-height:15.2px;color:#444}
  .empower-copy p+p{margin-top:15.2px}
  .center-photo{left:21px;top:200px;width:177px;height:123px;background:linear-gradient(160deg,#7fb2d8 0%,#1d4f7e 55%,#0f2a48 100%)}
  .meeting-photo{left:21px;top:338px;width:177px;height:172px;background:linear-gradient(160deg,#d0823b 0%,#6d6a66 50%,#2a3c5a 100%)}
</style>
</head>
<body>
<div class="canvas">

  <!-- outside of the brochure -->
  <section class="sheet sheet--outside">
    <div class="panel">
      <div class="photo team-photo" role="img" aria-label="Photo of a smiling home care scheduling team standing together in a bright office"></div>
      <h2 class="abs intro-head">COMPREHENSIVE ON-CALL<br>STAFFING SOLUTION</h2>
      <div class="abs intro-copy">
        <p>designed for home care by home care professionals. Experience seamless scheduling tailored to meet the unique needs of your clients and staff. Our team understands the demands of home care, ensuring that every shift is covered by qualified, compassionate caregivers.</p>
        <p>We prioritize flexibility and reliability, so you can focus on providing exceptional care while we handle the logistics. Whether you need last-minute coverage or regular scheduling support, our service is here to enhance your operation's efficiency and peace of mind. Let us help you get your weekends back and maintain the high standards your clients deserve.</p>
      </div>
    </div>

    <div class="panel panel--blue">
      <h1 class="abs cover-title"><span class="l1">HOME CARE</span><span class="l2">SCHEDULING</span></h1>
      <p class="abs cover-sub">Home Care scheduling by people<br>who know home care.</p>

      <div class="abs icon-tile" style="top:140px">
        <svg width="26" height="24" viewBox="0 0 26 24"><path d="M2 9 L13 1 L24 9 V23 H2 Z" fill="none" stroke="#0d4ea8" stroke-width="2"/><path d="M2 9 L13 17 L24 9" fill="none" stroke="#0d4ea8" stroke-width="2"/><circle cx="13" cy="9" r="3" fill="none" stroke="#0d4ea8" stroke-width="1.6"/></svg>
      </div>
      <p class="abs info-label" style="top:192px">Email Address:<br>jordanreyes@harborlinecare.com</p>

      <div class="abs icon-tile" style="top:245px">
        <svg width="20" height="26" viewBox="0 0 20 26"><path d="M10 1 C4.5 1 1 5 1 10 C1 17 10 25 10 25 C10 25 19 17 19 10 C19 5 15.5 1 10 1 Z" fill="#0d4ea8"/><circle cx="10" cy="10" r="3.5" fill="#fff"/></svg>
      </div>
      <p class="abs info-label" style="top:297px">Location:<br>Cedar Vale Texas</p>

      <div class="abs icon-tile" style="top:348px">
        <svg width="28" height="26" viewBox="0 0 28 26"><path d="M4 13 A10 10 0 0 1 24 13" fill="none" stroke="#0d4ea8" stroke-width="2"/><rect x="2" y="12" width="4" height="7" rx="1.5" fill="#0d4ea8"/><rect x="22" y="12" width="4" height="7" rx="1.5" fill="#0d4ea8"/><ellipse cx="14" cy="14" rx="7" ry="5.5" fill="#0d4ea8"/><circle cx="11" cy="14" r="1" fill="#fff"/><circle cx="14" cy="14" r="1" fill="#fff"/><circle cx="17" cy="14" r="1" fill="#fff"/><path d="M24 19 Q24 24 16 24" fill="none" stroke="#0d4ea8" stroke-width="1.6"/></svg>
      </div>
      <p class="abs info-label" style="top:400px">Support:</p>
      <p class="abs support-big">24/7 SERVICES</p>

      <div class="abs call-box">
        <div class="tile">
          <svg width="18" height="18" viewBox="0 0 18 18"><path d="M3 2 L6 2 L7.5 6 L5.5 7.5 C6.5 9.8 8.2 11.5 10.5 12.5 L12 10.5 L16 12 L16 15 C16 16 15 17 14 17 C7 16.5 1.5 11 1 4 C1 3 2 2 3 2 Z" fill="#fff"/></svg>
        </div>
        <span class="lbl">Call Us:</span>
        <span class="num">555.014.2287</span>
      </div>
    </div>

    <div class="panel">
      <div class="photo agent-photo" role="img" aria-label="Photo of a smiling scheduler in a dark blazer answering a desk phone"></div>
      <div class="abs brand-tile"><span class="sq"></span><span class="name">Tide Harbor</span></div>
      <p class="abs brand-name">TIDE HARBOR</p>
      <p class="abs brand-line">ON CALL SERVICE</p>
      <div class="abs rule" style="top:464px;left:22px;width:176px"></div>
      <p class="abs tagline">Get your weekends back</p>
      <div class="abs rule" style="top:487px;left:22px;width:176px"></div>
    </div>
  </section>

  <!-- inside of the brochure -->
  <section class="sheet sheet--inside">
    <div class="panel">
      <h2 class="abs sec-head" style="top:14px">OUR SERVICES</h2>

      <div class="abs service" style="top:41px">
        <div class="tile">
          <svg width="34" height="34" viewBox="0 0 34 34"><path d="M5 10 L9 10 L11 15 L8.5 17 C10 20 12.5 22.5 15.5 24 L17.5 21.5 L22.5 23.5 L22.5 27.5 C22.5 29 21 30 19.5 30 C10.5 29 4 22 3 13 C3 11 4 10 5 10 Z" fill="#fff"/><circle cx="23" cy="10" r="7.5" fill="none" stroke="#fff" stroke-width="2"/><path d="M23 6 V10 L26 12" fill="none" stroke="#fff" stroke-width="1.8"/></svg>
        </div>
        <h3>ON-CALL STAFFING</h3>
        <p>Our dedicated staffing teams answer your calls and respond as an extension of your agency</p>
      </div>

      <div class="abs service" style="top:118px">
        <div class="tile">
          <svg width="34" height="30" viewBox="0 0 34 30"><circle cx="17" cy="5" r="3" fill="#fff"/><circle cx="7" cy="9" r="2.6" fill="#fff"/><circle cx="27" cy="9" r="2.6" fill="#fff"/><path d="M2 19 Q7 12 12 19 Z M22 19 Q27 12 32 19 Z" fill="#fff"/><circle cx="16" cy="16" r="6" fill="none" stroke="#fff" stroke-width="2"/><circle cx="16" cy="15" r="2" fill="#fff"/><path d="M12.5 19.5 Q16 16 19.5 19.5" fill="#fff"/><path d="M20.5 20.5 L26 26" stroke="#fff" stroke-width="2.6" stroke-linecap="round"/></svg>
        </div>
        <h3>RECRUITING</h3>
        <p>Looking for the best caregivers? Let Tide harbor find qualified professionals for you.</p>
      </div>

      <div class="abs service" style="top:195px">
        <div class="tile">
          <svg width="34" height="34" viewBox="0 0 34 34"><circle cx="9" cy="9" r="6" fill="none" stroke="#fff" stroke-width="1.8"/><text x="9" y="12.5" font-size="9" font-family="Arial,sans-serif" font-weight="700" fill="#fff" text-anchor="middle">$</text><rect x="8" y="24" width="4" height="7" fill="#fff"/><rect x="14" y="20" width="4" height="11" fill="#fff"/><rect x="20" y="16" width="4" height="15" fill="#fff"/><rect x="26" y="11" width="4" height="20" fill="#fff"/><path d="M6 22 Q18 20 28 5" fill="none" stroke="#fff" stroke-width="1.8"/><path d="M24 5 L29 3 L29.5 8" fill="none" stroke="#fff" stroke-width="1.8"/><rect x="4" y="31" width="28" height="1.5" fill="#fff"/></svg>
        </div>
        <h3>INTAKE</h3>
        <p>Don't miss out on new revenue with our untake services</p>
      </div>

      <h2 class="abs sec-head" style="top:274px">YOUR AGENCY MATTERS</h2>
      <div class="abs matters-copy">
        <p>You will benefit from dedicated implementation staff, along with the reassurance that your agency is our highest priority. Our team is committed to understanding your unique needs and providing your unique needs and providing tailored solutions that enhance your agency's operations. From seamless onboarding to ongoing support, we ensure that every aspect of our service is designed to empower you and facilitate your success.</p>
        <p>With our expertise, you can focus on what truely matters - delivering exceptional care to your clients. Whether you're expanding your services or streamlining existing processes, we're here to support you every step of the way. Let us help you elevate your agency to new height, ensuring both your staff and clients experience the best possible outcomes.</p>
      </div>
    </div>

    <div class="panel panel--blue">
      <h2 class="abs band-top">US BASED STAFF</h2>
      <div class="photo headset-photo" role="img" aria-label="Photo of a smiling call agent wearing a headset and a green blazer"></div>
      <div class="abs band-bottom"></div>
      <p class="abs support-note">TIDE HARBOR IS SUPPORTED BY<br>U.S-BASED AGENTS AVAILABLE 24/7.</p>
      <p class="abs real">REAL</p>
      <p class="abs real-list">PEOPLE<br>ASSISTANCE<br>GROWTH</p>
      <div class="abs rule--light" style="top:477px;left:18px;width:182px;height:1px"></div>
      <p class="abs every">Every single time</p>
      <div class="abs rule--light" style="top:499px;left:18px;width:182px;height:1px"></div>
    </div>

    <div class="panel">
      <h2 class="abs empower">EMPOWER<br>YOUR AGENCY FOR<br>EXPANSION</h2>
      <div class="abs empower-copy">
        <p>Tide Harbor is not just an answering service.<br>We provide a comprehensive solution for<br>after-hours coverage.</p>
        <p>Say goodbye to expensive overtime costs<br>and the risk of staff burnout.</p>
      </div>
      <div class="photo center-photo" role="img" aria-label="Photo of a busy call center floor with agents at monitors in blue light"></div>
      <div class="photo meeting-photo" role="img" aria-label="Photo of a smiling agency team gathered around a meeting table with laptops"></div>
    </div>
  </section>

</div>
</body>
</html>
```